Double-Sided Table Top Flyer to Match Attached Marketing Materials

Please read this carefully. Must follow instructions. Do not submit multiple designs that look similar. Submit the front and back together as one submission. Do not submit the front and back separately. I have attached my new rack card design, business card design and gift card design. Colors, shapes and style match. I want a table top flyer to match them using same colors, shapes and style. The flyer will be 282.4 mm tall by 218.9 mm wide. See attached FLYER SPECs which shows full bleed, trim and safety area dimensions. THE FRONT: The main focus of the front is an "Harbor Sunset Drawing". This should be the main focus / font centered on the front. Under this there should be the attached paragraph. The front will also use the attached "PROFILE PIRATE" picture. The front will also incorporate my primary logo for "Skipper Dalloway's Sail Lessons & Cruises, LLC" as well as the badges of "Licensed Captain", "Instructor" and "Licensed Captain". Please incorporate the attached family beach day photo somehow. It may be set in the background as transparent. Designer's choice of how to incorporate. FOR THE BACK: Take most of the content from the front of the attached rack card. If additional content is required for the back please include as much as you can from the back of the attached rack card. The front has the three small pictures. The back has the one picture of me and the three logos towards the bottom. The content on the front of rack card takes priority over the content on back.

Target Market(s)

see attachments.

Industry/Entity Type

see attachments.

Font styles to use
Other font styles liked:
• The font type I use most is Good Timing RG from glyphbarnery.com

Requirements
Must have
• see attachments.
Nice to have
• see attachments.
Should not have
• see attachments.

```html
<!DOCTYPE html>
<html lang="en">
<head>
<meta charset="utf-8">
<title>Skipper Dalloway's Sail Lessons & Cruises — Table Top Flyer</title>
<link rel="stylesheet" href="https://fonts.googleapis.com/css2?family=Saira:wght@500;700&family=Cinzel:wght@400&family=Great+Vibes&family=Lato:wght@400;700&display=swap">
<style>
:root{
  --stage:#8b8b8b;
  --navy:#1b2f52;
  --navy-deep:#13223d;
  --red:#d81f45;
  --gold:#e4ad2b;
  --ink:#1c1c1c;
  --white:#ffffff;
  --sea:#c9d6e2;
}
*{margin:0;padding:0;box-sizing:border-box}
html,body{width:1200px;height:1200px;overflow:hidden;background:var(--stage)}
.canvas{position:relative;width:1200px;height:1200px}
.flyer{position:absolute;top:240px;width:533px;height:690px;background:var(--white);overflow:hidden;box-shadow:0 4px 14px rgba(0,0,0,.35);font-family:"Lato",sans-serif}
.flyer--front{left:48px}
.flyer--back{left:617px}
.shapes{position:absolute;inset:0}
.brand-header{position:absolute;top:22px;left:0;width:100%;text-align:center;font-family:"Saira",sans-serif;font-weight:700;font-size:21px;line-height:1.2;color:var(--white);letter-spacing:.5px}
.brand-header span{color:var(--gold)}
.flyer--back .brand-header{left:14px;width:505px;top:10px;border:1px solid rgba(255,255,255,.8);padding:5px 0 4px}
.brand-seal{position:absolute;border-radius:50%;background:var(--white);border:5px solid var(--gold);display:flex;align-items:center;justify-content:center;text-align:center;font-family:"Saira",sans-serif;font-weight:700;color:var(--navy);line-height:1.15}
.event-title{position:absolute;left:222px;top:70px;width:300px;text-align:center;color:var(--white);font-family:"Cinzel",serif;font-size:42px;font-weight:400;line-height:1.05}
.event-title .script{display:block;font-family:"Great Vibes",cursive;color:var(--gold);font-size:60px;line-height:1;margin-top:2px;padding-left:70px}
.photo{position:absolute}
.details-box{position:absolute;left:24px;top:214px;width:192px;height:292px;background:var(--ink);border:2px solid var(--red);border-radius:26px 0 0 0;padding:24px 14px 10px 14px;color:var(--white);font-size:10.6px;line-height:1.35;text-align:right}
.details-box p{margin-bottom:11px}
.details-box b{color:var(--gold);font-weight:700;font-size:11.5px}
.details-box em{color:var(--gold);font-style:italic;font-weight:700;font-size:11.5px}
.badge{position:absolute;width:64px;height:64px;border-radius:50%;border:4px solid var(--white);box-shadow:0 0 0 2px #c9ced8}
.phone-pill{position:absolute;left:24px;width:194px;height:32px;border-radius:16px;background:var(--gold);display:flex;align-items:center;gap:10px;padding-left:5px;font-family:"Saira",sans-serif;font-weight:700;font-size:19px;color:var(--ink)}
.phone-pill .icon{width:23px;height:23px;border-radius:50%;background:var(--red);display:flex;align-items:center;justify-content:center}
.email{position:absolute;left:24px;font-size:12.5px;color:var(--white);display:flex;align-items:center;gap:6px}
.email i{width:11px;height:11px;border-radius:50%;background:var(--gold);display:inline-block}
.web{position:absolute;right:10px;font-family:"Saira",sans-serif;font-weight:700;font-size:18px;color:var(--white)}
.web span{color:var(--gold)}
.intro{position:absolute;left:26px;top:60px;width:481px;color:var(--white);font-size:9.4px;line-height:1.3;text-align:center}
.intro p+p{margin-top:9px}
.ring{position:absolute;border-radius:50%;border:4px solid var(--red);box-shadow:0 0 0 2px var(--white)}
.services-title{position:absolute;left:223px;top:302px;width:168px;height:28px;border-radius:14px;background:var(--gold);color:var(--white);font-family:"Saira",sans-serif;font-weight:700;font-size:18px;text-align:center;line-height:28px}
.service{position:absolute;display:flex;align-items:center;gap:8px;font-family:"Saira",sans-serif;font-weight:500;font-size:9.6px;line-height:1.1;color:#333;text-transform:uppercase;width:140px}
.service i{flex:none;width:26px;height:26px;border-radius:50%;display:flex;align-items:center;justify-content:center}
.service i::after{content:"";width:9px;height:9px;border-radius:2px;background:var(--white)}
.service .red{background:var(--red)}
.service .gold{background:var(--gold)}
.owner{position:absolute;left:0;top:556px;width:211px;height:58px;background:var(--red);color:var(--white);text-align:center;font-family:"Saira",sans-serif;padding-top:7px;line-height:1.2}
.owner b{display:block;color:var(--gold);font-size:15px;font-weight:700}
.owner span{display:block;font-size:15px;font-weight:500}
.credential{position:absolute;top:540px;width:80px;text-align:center;color:var(--white);font-family:"Saira",sans-serif;font-size:10px;line-height:1.15}
.credential i{display:block;margin:0 auto 5px;width:34px;height:34px;border-radius:50%;background:var(--red);border:3px solid var(--white)}
</style>
</head>
<body>
<div class="canvas">

  <section class="flyer flyer--front">
    <svg class="shapes" width="533" height="690" viewBox="0 0 533 690">
      <defs>
        <linearGradient id="frontSky" x1="0" y1="0" x2="1" y2="1">
          <stop offset="0" stop-color="#1b2f52"/>
          <stop offset="1" stop-color="#2c456d"/>
        </linearGradient>
      </defs>
      <path d="M0 0H533V292Q420 332 300 300Q170 262 0 220Z" fill="#d81f45"/>
      <path d="M0 0H533V276Q420 316 300 284Q170 246 0 204Z" fill="url(#frontSky)"/>
      <rect x="0" y="634" width="533" height="56" fill="#1c1c1c"/>
      <path d="M282 650H533V690H268Q272 660 282 650Z" fill="#d81f45"/>
    </svg>

    <h2 class="brand-header">SKIPPER DALLOWAY'S <span>SAIL &amp; CRUISES</span></h2>

    <div class="brand-seal" style="left:34px;top:80px;width:142px;height:142px;font-size:13px">Skipper<br>Dalloway's</div>

    <h1 class="event-title">HARBOR<br>SUNSET<span class="script">Drawing</span></h1>

    <div class="photo" role="img" aria-label="Smiling captain in pirate costume holding a skull flag aboard a boat"
         style="left:226px;top:250px;width:307px;height:384px;background:linear-gradient(160deg,#3a3f4d 0%,#6d6a6e 45%,#c9b7a6 75%,#e8e2db 100%)"></div>

    <div class="details-box">
      <p><b>This harbor drawing</b><br>is for a boat outing leaving from Bayhaven going to a barrier island such as Gull Key or Pelican Bar.</p>
      <p><b>This package includes</b><br>the boat, a licensed captain and fuel. The duration will be approximately four to six hours.</p>
      <p><em>The winner of drawing</em><br>may bring up to a total of six passengers. The winner is responsible for their own provisions such as ice, drinks and food.</p>
    </div>

    <div class="badge" style="left:22px;top:522px;background:#dfe6ef"></div>
    <div class="badge" style="left:90px;top:522px;background:var(--navy)"></div>
    <div class="badge" style="left:158px;top:522px;background:var(--red)"></div>

    <div class="phone-pill" style="top:602px">
      <span class="icon"><svg width="13" height="13" viewBox="0 0 24 24"><path d="M6.6 10.8a15 15 0 0 0 6.6 6.6l2.2-2.2c.3-.3.7-.4 1-.2 1.1.4 2.3.6 3.6.6.6 0 1 .4 1 1V20c0 .6-.4 1-1 1A17 17 0 0 1 3 4c0-.6.4-1 1-1h3.5c.6 0 1 .4 1 1 0 1.3.2 2.5.6 3.6.1.3 0 .7-.2 1z" fill="#fff"/></svg></span>
      (555) 014 - 2876
    </div>
    <div class="email" style="top:660px"><i></i>hello@hireaskipper.com</div>
    <div class="web" style="top:658px">WWW.<span>HIRE-A-SKIPPER</span>.COM</div>
  </section>

  <section class="flyer flyer--back">
    <svg class="shapes" width="533" height="690" viewBox="0 0 533 690">
      <defs>
        <linearGradient id="backSky" x1="0" y1="0" x2="1" y2="1">
          <stop offset="0" stop-color="#1b2f52"/>
          <stop offset="1" stop-color="#28416a"/>
        </linearGradient>
        <linearGradient id="backSea" x1="0" y1="0" x2="0" y2="1">
          <stop offset="0" stop-color="#f4f6f9"/>
          <stop offset="1" stop-color="#c9d6e2"/>
        </linearGradient>
      </defs>
      <rect x="0" y="140" width="533" height="420" fill="url(#backSea)"/>
      <path d="M0 0H533V158Q380 200 266 188Q130 176 0 226Z" fill="#d81f45"/>
      <path d="M0 0H533V142Q380 184 266 172Q130 160 0 210Z" fill="url(#backSky)"/>
      <rect x="211" y="550" width="322" height="100" fill="#1b2f52"/>
      <rect x="0" y="650" width="533" height="40" fill="#1c1c1c"/>
      <path d="M282 660H533V690H270Q274 666 282 660Z" fill="#d81f45"/>
    </svg>

    <h2 class="brand-header">SKIPPER DALLOWAY'S <span>SAIL &amp; CRUISES</span></h2>

    <div class="intro">
      <p>Maritime Authority Licensed Master Captain &amp; Coastal Safe Boating Board Certified Boating Instructor providing hands-on boat training &amp; captaining services with your boat at your location.</p>
      <p>Don't overpay elsewhere. All training that is conducted by any qualified person or company is based of nationally accredited &amp; recognized content &amp; curriculum developed by the Coastal Safe Boating Board; or the Allied Harbor Squadrons</p>
    </div>

    <div class="ring" role="img" aria-label="Child in a life jacket looking through binoculars" style="left:6px;top:146px;width:88px;height:88px;background:linear-gradient(160deg,#9cb6c9,#d9733d)"></div>
    <div class="ring" role="img" aria-label="Person kneeling on the beach in a blue shirt" style="left:118px;top:158px;width:88px;height:88px;background:linear-gradient(160deg,#c9b49a,#3a63b0)"></div>
    <div class="brand-seal" style="left:210px;top:140px;width:122px;height:122px;font-size:11.5px">Skipper<br>Dalloway's</div>
    <div class="ring" role="img" aria-label="Woman smiling at the helm of a boat" style="left:332px;top:158px;width:88px;height:88px;background:linear-gradient(160deg,#e6e8ea,#5b4a44)"></div>
    <div class="ring" role="img" aria-label="Boater working at a dock in the sun" style="left:426px;top:128px;width:88px;height:88px;background:linear-gradient(160deg,#8d8f93,#3b78b5)"></div>

    <div class="photo" role="img" aria-label="Portrait of the owner and captain in a grey polo with lanyard"
         style="left:0;top:298px;width:211px;height:258px;background:linear-gradient(180deg,#1a1a1a,#3e3e3e 60%,#8f9297);border-top:3px solid var(--red);border-right:3px solid var(--red);border-radius:0 36px 0 0"></div>

    <div class="services-title">OUR SERVICES</div>
    <div class="service" style="left:229px;top:350px"><i class="red"></i>Introduction to power boating</div>
    <div class="service" style="left:388px;top:345px"><i class="red"></i>Hands-on boat training</div>
    <div class="service" style="left:229px;top:397px"><i class="gold"></i>Precision docking &amp; boat handling</div>
    <div class="service" style="left:388px;top:397px"><i class="gold"></i>Coastal navigation</div>
    <div class="service" style="left:229px;top:440px"><i class="red"></i>Captaining/ piloting service to your outing</div>
    <div class="service" style="left:388px;top:440px"><i class="red"></i>Open water boat handling</div>
    <div class="service" style="left:229px;top:482px"><i class="gold"></i>Open water advanced maneuvers</div>

    <div class="credential" style="left:226px"><i></i>Retired<br>Military</div>
    <div class="credential" style="left:340px"><i></i>Current<br>Security<br>Clearance</div>
    <div class="credential" style="left:448px"><i></i>Graduate<br>Degree</div>

    <div class="owner"><b>DALTON R. WHITCOMBE</b><span>OWNER &amp; CAPTAIN</span></div>

    <div class="phone-pill" style="top:618px">
      <span class="icon"><svg width="13" height="13" viewBox="0 0 24 24"><path d="M6.6 10.8a15 15 0 0 0 6.6 6.6l2.2-2.2c.3-.3.7-.4 1-.2 1.1.4 2.3.6 3.6.6.6 0 1 .4 1 1V20c0 .6-.4 1-1 1A17 17 0 0 1 3 4c0-.6.4-1 1-1h3.5c.6 0 1 .4 1 1 0 1.3.2 2.5.6 3.6.1.3 0 .7-.2 1z" fill="#fff"/></svg></span>
      (555) 014 - 2876
    </div>
    <div class="email" style="top:666px"><i></i>hello@hireaskipper.com</div>
    <div class="web" style="top:663px">WWW.<span>HIRE-A-SKIPPER</span>.COM</div>
  </section>

</div>
</body>
</html>
```